Moravel Swim Stationary

Recently established Aquatics Club, with competitive swimming being a principal activity needs stationary, including business cards, letterhead and envelopes, application forms.
The designs shold incorporate the Club's logo. ( The colours are aqua and teal)
The statonary should be fun yet project a corporate image sufficient to attract potential sponsors.

Club members, sponsors, professional organisations.

Business

• Club Logo
Address & Telephone number

The letterhead must contain the Club's Mission Statement.
It can be incorporated in the "footer" on the page.

To provide aquatics programmes, for persons of all ages, that encourage physical fitness and wellness, build character and self-discipline, inspire camaraderie and promote civic mindedness and excellence.

```html
<!DOCTYPE html>
<html lang="en">
<head>
<meta charset="utf-8">
<title>Moravel Swim Stationery</title>
<link rel="stylesheet" href="https://fonts.googleapis.com/css2?family=Open+Sans:wght@400;600&display=swap">
<style>
:root{
  --teal:#079a8a;
  --orange:#ef6a0c;
  --paper:#ffffff;
  --ink:#222222;
  --backdrop:#e9e9e9;
  --teal-faint:rgba(7,154,138,.12);
  --orange-faint:rgba(239,106,12,.12);
}
*{box-sizing:border-box;margin:0;padding:0}
html,body{width:1200px;height:888px;overflow:hidden}
body{background:var(--backdrop);font-family:"Open Sans",Arial,sans-serif;color:var(--ink);position:relative}
.sheet{position:absolute;background:var(--paper);box-shadow:0 2px 6px rgba(0,0,0,.12);overflow:hidden}
.brand{display:flex;align-items:center;gap:6px;font-weight:600;color:var(--orange);white-space:nowrap}
.brand-dot{border-radius:50%;background:var(--teal);flex:none}
.contact{list-style:none;font-size:8px;line-height:1.5}
.contact li{display:flex;align-items:center;gap:5px}
.icon{width:7px;height:7px;background:var(--orange);flex:none}
.watermark{position:absolute;border-radius:50%;background:var(--orange-faint)}

/* letterhead */
.letterhead{left:40px;top:40px;width:330px;height:467px}
.letterhead .brand{position:absolute;left:24px;top:24px;font-size:14px}
.letterhead .brand-dot{width:10px;height:10px}
.letterhead .contact{position:absolute;right:28px;top:74px;font-size:6.5px}
.letterhead .rule{position:absolute;right:20px;top:74px;width:2px;height:46px;background:var(--teal)}
.letterhead .watermark{width:130px;height:130px;right:40px;bottom:16px}
.bar-orange{position:absolute;height:8px;background:var(--orange)}
.bar-teal{position:absolute;height:8px;background:var(--teal)}
.letterhead .bar-orange{left:0;bottom:14px;width:170px}
.letterhead .bar-teal{left:170px;right:0;bottom:6px}

/* folder */
.folder{left:400px;top:40px;width:330px;height:467px}
.folder .brand{position:absolute;left:0;right:0;top:58px;justify-content:center;font-size:18px}
.folder .brand-dot{width:12px;height:12px}
.folder .panel{position:absolute;left:0;right:0;top:130px;bottom:0;background:var(--teal)}
.folder .panel::before{content:"";position:absolute;left:0;right:0;top:8px;height:2px;background:rgba(255,255,255,.8)}
.folder .panel-mark{position:absolute;right:30px;bottom:50px;width:160px;height:160px;border-radius:50%;background:rgba(255,255,255,.12)}
.folder .footer{position:absolute;left:18px;right:18px;bottom:18px;display:flex;justify-content:space-between;align-items:flex-end;color:#fff;font-size:7px}
.folder .footer .contact{font-size:7px}

/* business cards */
.card{width:340px;height:195px}
.card-front{left:770px;top:40px}
.card-front .brand{position:absolute;left:24px;top:22px;font-size:14px}
.card-front .brand-dot{width:10px;height:10px}
.card-front .band{position:absolute;left:0;right:0;top:92px;height:72px;background:var(--orange);color:#fff;padding:14px 24px}
.card-front .name{font-size:14px;font-weight:600}
.card-front .role{font-size:9px}
.card-front .band .contact{position:absolute;right:24px;top:12px;font-size:8px}
.card-front .band .icon{background:#fff}
.card-front .base{position:absolute;left:0;right:0;bottom:0;height:14px;background:var(--teal)}
.card-back{left:770px;top:275px;background:var(--teal)}
.card-back .web{position:absolute;left:22px;top:20px;color:#fff;font-size:9px}
.card-back .brand{position:absolute;left:0;right:0;top:82px;justify-content:center;font-size:22px;color:#fff}
.card-back .brand-dot{width:14px;height:14px;background:#fff}

/* envelopes */
.envelope{width:540px;height:270px}
.envelope-front{left:40px;top:560px}
.envelope-front .brand{position:absolute;left:44px;top:26px;font-size:14px}
.envelope-front .brand-dot{width:10px;height:10px}
.envelope-front .rule{position:absolute;left:24px;top:76px;width:2px;height:50px;background:var(--teal)}
.envelope-front .contact{position:absolute;left:36px;top:76px;font-size:9px}
.envelope-front .watermark{width:140px;height:140px;right:60px;bottom:10px}
.envelope-front .bar-orange{left:0;bottom:22px;width:300px}
.envelope-front .bar-teal{left:300px;right:0;bottom:12px}
.envelope-back{left:620px;top:560px}
.envelope-back .flap{position:absolute;left:0;right:0;top:40px;height:110px;background:var(--orange);display:flex;align-items:center;justify-content:center}
.envelope-back .brand{color:#fff;font-size:16px}
.envelope-back .brand-dot{width:11px;height:11px;background:#fff}
</style>
</head>
<body>

<section class="sheet letterhead" aria-label="Letterhead">
  <div class="brand"><span class="brand-dot"></span>Moravel Swim</div>
  <ul class="contact">
    <li><span class="icon"></span>Street Address here</li>
    <li><span class="icon"></span>Somewhere Suite</li>
    <li><span class="icon"></span>000 111 2222</li>
    <li><span class="icon"></span>info@moravelswim.com</li>
    <li><span class="icon"></span>www.moravelswim.com</li>
  </ul>
  <span class="rule"></span>
  <span class="watermark"></span>
  <span class="bar-orange"></span><span class="bar-teal"></span>
</section>

<section class="sheet folder" aria-label="Presentation folder">
  <div class="brand"><span class="brand-dot"></span>Moravel Swim</div>
  <div class="panel">
    <span class="panel-mark"></span>
    <div class="footer">
      <ul class="contact">
        <li><span class="icon"></span>Street Address here, Somewhere Suite</li>
        <li><span class="icon"></span>000 111 2222</li>
        <li><span class="icon"></span>info@moravelswim.com</li>
      </ul>
      <ul class="contact"><li><span class="icon"></span>www.moravelswim.com</li></ul>
    </div>
  </div>
</section>

<section class="sheet card card-front" aria-label="Business card front">
  <div class="brand"><span class="brand-dot"></span>Moravel Swim</div>
  <div class="band">
    <p class="name">Dana Kettering</p>
    <p class="role">Manager</p>
    <ul class="contact">
      <li><span class="icon"></span>Street Address here</li>
      <li><span class="icon"></span>000 111 2222</li>
      <li><span class="icon"></span>info@moravelswim.com</li>
      <li><span class="icon"></span>www.moravelswim.com</li>
    </ul>
  </div>
  <span class="base"></span>
</section>

<section class="sheet card card-back" aria-label="Business card back">
  <p class="web">www.moravelswim.com</p>
  <div class="brand"><span class="brand-dot"></span>Moravel Swim</div>
</section>

<section class="sheet envelope envelope-front" aria-label="Envelope front">
  <div class="brand"><span class="brand-dot"></span>Moravel Swim</div>
  <span class="rule"></span>
  <ul class="contact">
    <li><span class="icon"></span>Street Address here</li>
    <li><span class="icon"></span>Somewhere Suite</li>
    <li><span class="icon"></span>000 111 2222</li>
    <li><span class="icon"></span>info@moravelswim.com</li>
    <li><span class="icon"></span>www.moravelswim.com</li>
  </ul>
  <span class="watermark"></span>
  <span class="bar-orange"></span><span class="bar-teal"></span>
</section>

<section class="sheet envelope envelope-back" aria-label="Envelope back">
  <div class="flap"><div class="brand"><span class="brand-dot"></span>Moravel Swim</div></div>
</section>

</body>
</html>
```